Lumara Health & Wellness Business Card Design

We would like to create business cards matching with our new logo design. The card should be professional looking but still have a playful side and something that would be eye catching. We are planing to open a luxury medical spa and looking to create a design based on this new logo. We are looking for a design that shows off luxury but not be gold in color. Also, while we are a more female oriented medical center we do have men that come in for our services and it should be be too feminine.

Target Market(s)

Health & Wellness. Medical patients. Luxury spa

Industry/Entity Type

Health And Wellness

Contact Information for Business Card

It should have the logo design in the front of card and back of card should have our contact information. Our current colors are peach/ coral, teal, and gray. We are looking for a modern looking design.

Font styles to use
Script

Colors
32a6d6
e667a6
86cfc6
fece3e

Requirements
Must have
• It should have our logo design. We would prefer to have a more modern look to the card.
Nice to have
• Eye-Catching Design on the personable side but still classy.
Should not have
• At this point we are looking for the best design. It should not have color purple.

```html
<!DOCTYPE html>
<html lang="en">
<head>
<meta charset="utf-8">
<title>Lumara Health &amp; Wellness – Business Cards</title>
<link rel="stylesheet" href="https://fonts.googleapis.com/css2?family=PT+Sans:wght@400;700&display=swap">
<style>
  :root {
    --bg: #dcdddf;
    --pink: #e667a6;
    --blue: #32a6d6;
    --teal: #4fb7aa;
    --yellow: #ebbd1c;
    --ink: #1d1d1f;
    --paper: #ffffff;
  }
  * { margin: 0; padding: 0; box-sizing: border-box; }
  html, body { width: 1200px; height: 833px; overflow: hidden; background: var(--bg); }
  body { font-family: "PT Sans", Arial, sans-serif; position: relative; }

  .card {
    position: absolute;
    width: 334px; height: 334px;
    border-radius: 18px;
    overflow: hidden;
  }
  .card--pink   { left: 66px;  top: 66px;  background: var(--pink); }
  .card--blue   { left: 433px; top: 66px;  background: var(--blue); }
  .card--teal   { left: 66px;  top: 433px; background: var(--teal); }
  .card--yellow { left: 433px; top: 433px; background: var(--yellow); }
  .card--back   { background: var(--paper); box-shadow: 0 1px 3px rgba(0,0,0,.08); }
  .card--back-a { left: 800px; top: 66px; }
  .card--back-b { left: 800px; top: 433px; }

  .wordmark {
    position: absolute;
    color: var(--paper);
    font-weight: 400;
    text-align: center;
    line-height: 1;
  }
  .card--front .wordmark { left: 0; right: 0; top: 118px; }
  .wordmark__name { font-size: 68px; letter-spacing: 1px; display: block; }
  .wordmark__tag  { font-size: 17px; letter-spacing: .5px; display: block; margin-top: 10px; font-variant: small-caps; }

  .card--back .wordmark { color: var(--ink); left: 118px; width: 210px; top: 52px; }
  .card--back .wordmark__name { font-size: 46px; }
  .card--back .wordmark__tag  { font-size: 13px; margin-top: 7px; }

  .contact {
    position: absolute;
    left: 18px; top: 243px;
    list-style: none;
    font-size: 13px;
    color: var(--ink);
  }
  .contact li { display: flex; align-items: center; height: 19px; }
  .contact .icon {
    width: 18px; height: 18px; margin-right: 7px;
    display: flex; align-items: center; justify-content: center;
  }
  .icon--phone { background: var(--pink); }
  .icon--mail  { background: var(--blue); }
  .icon--pin   { background: var(--teal); }
  .icon--web   { background: var(--yellow); }
  .card--back-b .contact { top: 297px; top: 240px; }
  .site-line {
    position: absolute; left: 18px; top: 305px;
    font-size: 13px; font-weight: 700; color: var(--ink);
  }
</style>
</head>
<body>

  <div class="card card--front card--pink">
    <div class="wordmark"><span class="wordmark__name">Lumara</span><span class="wordmark__tag">Health, Wellness &amp; Beauty</span></div>
  </div>
  <div class="card card--front card--blue">
    <div class="wordmark"><span class="wordmark__name">Lumara</span><span class="wordmark__tag">Health, Wellness &amp; Beauty</span></div>
  </div>
  <div class="card card--front card--teal">
    <div class="wordmark"><span class="wordmark__name">Lumara</span><span class="wordmark__tag">Health, Wellness &amp; Beauty</span></div>
  </div>
  <div class="card card--front card--yellow">
    <div class="wordmark"><span class="wordmark__name">Lumara</span><span class="wordmark__tag">Health, Wellness &amp; Beauty</span></div>
  </div>

  <div class="card card--back card--back-a">
    <div class="wordmark"><span class="wordmark__name">Lumara</span><span class="wordmark__tag">Health, Wellness &amp; Beauty</span></div>
    <ul class="contact">
      <li><span class="icon icon--phone"><svg width="12" height="12" viewBox="0 0 24 24"><path fill="#fff" d="M6.6 10.8a15 15 0 0 0 6.6 6.6l2.2-2.2c.3-.3.7-.4 1-.2 1.1.4 2.3.6 3.6.6.6 0 1 .4 1 1V20c0 .6-.4 1-1 1A17 17 0 0 1 3 4c0-.6.4-1 1-1h3.5c.6 0 1 .4 1 1 0 1.3.2 2.5.6 3.6.1.3 0 .7-.2 1z"/></svg></span>(555) 014-2236</li>
      <li><span class="icon icon--mail"><svg width="12" height="10" viewBox="0 0 24 18"><rect x="1" y="1" width="22" height="16" fill="none" stroke="#fff" stroke-width="2"/><path d="M1 1l11 9 11-9" fill="none" stroke="#fff" stroke-width="2"/></svg></span>info@lumarawellness.com</li>
      <li><span class="icon icon--pin"><svg width="10" height="13" viewBox="0 0 20 26"><path fill="#fff" d="M10 0a9 9 0 0 0-9 9c0 7 9 17 9 17s9-10 9-17a9 9 0 0 0-9-9zm0 13a4 4 0 1 1 0-8 4 4 0 0 1 0 8z"/></svg></span>42 Linden Ave, Suite 4, Fairview, NJ 07000</li>
      <li><span class="icon icon--web"><svg width="12" height="12" viewBox="0 0 24 24" fill="none" stroke="#fff" stroke-width="2"><circle cx="12" cy="12" r="10"/><path d="M2 12h20M12 2c3 3 3 17 0 20M12 2c-3 3-3 17 0 20"/></svg></span>www.lumarawellness.com</li>
    </ul>
  </div>

  <div class="card card--back card--back-b">
    <div class="wordmark"><span class="wordmark__name">Lumara</span><span class="wordmark__tag">Health, Wellness &amp; Beauty</span></div>
    <ul class="contact">
      <li><span class="icon icon--phone"><svg width="12" height="12" viewBox="0 0 24 24"><path fill="#fff" d="M6.6 10.8a15 15 0 0 0 6.6 6.6l2.2-2.2c.3-.3.7-.4 1-.2 1.1.4 2.3.6 3.6.6.6 0 1 .4 1 1V20c0 .6-.4 1-1 1A17 17 0 0 1 3 4c0-.6.4-1 1-1h3.5c.6 0 1 .4 1 1 0 1.3.2 2.5.6 3.6.1.3 0 .7-.2 1z"/></svg></span>(555) 014-2236</li>
      <li><span class="icon icon--mail"><svg width="12" height="10" viewBox="0 0 24 18"><rect x="1" y="1" width="22" height="16" fill="none" stroke="#fff" stroke-width="2"/><path d="M1 1l11 9 11-9" fill="none" stroke="#fff" stroke-width="2"/></svg></span>info@lumarawellness.com</li>
      <li><span class="icon icon--pin"><svg width="10" height="13" viewBox="0 0 20 26"><path fill="#fff" d="M10 0a9 9 0 0 0-9 9c0 7 9 17 9 17s9-10 9-17a9 9 0 0 0-9-9zm0 13a4 4 0 1 1 0-8 4 4 0 0 1 0 8z"/></svg></span>42 Linden Ave, Suite 4, Fairview, NJ 07000</li>
    </ul>
    <div class="site-line">www.LUMARAWELLNESS.com</div>
  </div>

</body>
</html>
```